依頼詳細
女性警察官募集パフンレットの表紙のみA5サイズ一枚を依頼します。継続案件あります。素材は写真二枚を提供しますので、二枚とも使用するか、あるいは制服姿のみ一枚を使用してください。トリミング自由です。映り込みは加工しても構いませんが人物は加工不可です。テキストは指定のもののみ使用です。納品はイラストレーターです。印刷原稿ですので300dpiで作成してください。背景色やグラデーションを使用する場合は制服の水色を使用してください。
記載項目
タイトルは 女性警察官募集 サブタイトルは括弧付きで 「警察官に、なってみませんか」 です。「」と句点をつけてください。読点はつけません。
希望イメージ
シンプル 複雑
単色 カラフル
暗い 明るい
日常 高級
遊び心 厳粛
未来的 伝統的
女性的 男性的
希望する色
青系、水色系、制服写真のシャツの水色を基調にしてください
納品ファイル
• イラストレーター形式 (.ai)
補足説明
写真は背景をカットしないほうが良いですが写り込みはボカしても良いです。
タイトルテキストには装飾を周囲につけても構いません。イタリック体は使用不可です。横書き、縦書き、自由です。
人物の大きさが二つの写真で違うので、両方を使用する場合は人物のサイズを統一していただけると採用率が上がります。
また、ポーズが似ているので、仕事・プライペートの対比とする案、鏡のように並べる案、なども考えられます。斬新なアイデアを希望します。
指定した文字列以外は使用禁止です。増やしたものは採用しません。よろしくお願い致します。
ご応募有り難うございます。思いの外、応募をたくさん戴きましたので締め切りを早めさせていただきます。準備されていた方のことも考慮して、次の日曜日に致します。10月6日(日)です。また、選定確約しました。現在の応募の中に有力候補が複数あります。これを上回るデザインがあればお願いいたします。

ダイナミックな動きを感じるデザインは飛び抜けていました。

たくさんの応募有り難うございました。最初の提案から背景処理を施している方の作品はやはり着目します。(余計なものを消す、など)社内では他の作品も好評なものがありましたが、依頼主の選択で決まりました。次回も是非ご参加ください。

```html
<!DOCTYPE html>
<html lang="ja">
<head>
<meta charset="UTF-8">
<title>女性警察官募集</title>
<link rel="stylesheet" href="https://fonts.googleapis.com/css2?family=Noto+Sans+JP:wght@400;500&display=swap">
<style>
  :root {
    --sky-deep: #6fb6e6;
    --sky-mid: #a9d6f3;
    --sky-pale: #e3f2fc;
    --glow: #ffffff;
    --title-blue: #2b78c6;
    --ink: #3a3f47;
    --ring: rgba(255,255,255,0.85);
    --civil-tone: #d9cfc4;
    --uniform-tone: #8fc3e8;
  }
  * { margin: 0; padding: 0; box-sizing: border-box; }
  html, body { width: 849px; height: 1200px; overflow: hidden; }
  body { font-family: "Noto Sans JP", sans-serif; }
  .cover {
    position: relative;
    width: 849px;
    height: 1200px;
    overflow: hidden;
    background: linear-gradient(180deg, var(--sky-mid) 0%, var(--sky-deep) 45%, var(--sky-mid) 70%, var(--sky-pale) 100%);
  }
  .cover-art { position: absolute; inset: 0; }
  .subtitle {
    position: absolute;
    top: 738px;
    left: 0;
    width: 100%;
    text-align: center;
    font-size: 30px;
    font-weight: 400;
    color: var(--ink);
    letter-spacing: 1px;
  }
  .title {
    position: absolute;
    top: 815px;
    left: 0;
    width: 100%;
    text-align: center;
    font-size: 74px;
    font-weight: 500;
    color: var(--title-blue);
    letter-spacing: 8px;
  }
</style>
</head>
<body>
<main class="cover">
  <svg class="cover-art" width="849" height="1200" viewBox="0 0 849 1200" xmlns="http://www.w3.org/2000/svg">
    <defs>
      <radialGradient id="glow" cx="0.5" cy="0.5" r="0.5">
        <stop offset="0" stop-color="#ffffff" stop-opacity="0.95"/>
        <stop offset="0.6" stop-color="#ffffff" stop-opacity="0.55"/>
        <stop offset="1" stop-color="#ffffff" stop-opacity="0"/>
      </radialGradient>
      <linearGradient id="civilPhoto" x1="0" y1="0" x2="0" y2="1">
        <stop offset="0" stop-color="#a7b7a0"/>
        <stop offset="0.5" stop-color="var(--civil-tone)"/>
        <stop offset="1" stop-color="#f2efea"/>
      </linearGradient>
      <linearGradient id="uniformPhoto" x1="0" y1="0" x2="0" y2="1">
        <stop offset="0" stop-color="#b7cfd8"/>
        <stop offset="0.5" stop-color="var(--uniform-tone)"/>
        <stop offset="1" stop-color="#3e5a8c"/>
      </linearGradient>
      <clipPath id="photoCircle">
        <circle cx="424" cy="150" r="440"/>
      </clipPath>
    </defs>

    <ellipse class="glow" cx="424" cy="760" rx="520" ry="260" fill="url(#glow)"/>

    <g class="ring-lines" fill="none" stroke="var(--ring)">
      <circle cx="424" cy="150" r="455" stroke-width="3"/>
      <circle cx="424" cy="150" r="475" stroke-width="1.5" stroke-opacity="0.7"/>
      <circle cx="424" cy="150" r="500" stroke-width="1" stroke-opacity="0.5"/>
    </g>

    <g clip-path="url(#photoCircle)">
      <rect x="0" y="0" width="424" height="608" fill="url(#civilPhoto)" role="img" aria-label="Photo of a smiling woman in a white blouse, saluting playfully, off duty"/>
      <rect x="424" y="0" width="425" height="608" fill="url(#uniformPhoto)" role="img" aria-label="Photo of a smiling female police officer in a light blue uniform shirt and cap, saluting"/>
      <line x1="424" y1="0" x2="424" y2="608" stroke="#ffffff" stroke-width="4"/>
    </g>

    <g class="play-button">
      <circle cx="424" cy="285" r="56" fill="#2f7fc9" stroke="#ffffff" stroke-width="6"/>
      <path d="M406 255 L456 285 L406 315 Z" fill="#ffffff"/>
    </g>

    <g class="sparkles" fill="#ffffff">
      <path d="M120 980 l4 12 12 4 -12 4 -4 12 -4 -12 -12 -4 12 -4z"/>
      <path d="M720 1000 l3 9 9 3 -9 3 -3 9 -3 -9 -9 -3 9 -3z"/>
      <path d="M640 700 l3 9 9 3 -9 3 -3 9 -3 -9 -9 -3 9 -3z"/>
      <path d="M200 690 l3 9 9 3 -9 3 -3 9 -3 -9 -9 -3 9 -3z"/>
      <path d="M780 760 l4 12 12 4 -12 4 -4 12 -4 -12 -12 -4 12 -4z"/>
      <path d="M420 1080 l3 9 9 3 -9 3 -3 9 -3 -9 -9 -3 9 -3z"/>
      <circle cx="80" cy="800" r="3"/><circle cx="300" cy="1010" r="2.5"/>
      <circle cx="560" cy="1040" r="3"/><circle cx="700" cy="900" r="2.5"/>
      <circle cx="160" cy="1120" r="2"/><circle cx="760" cy="1130" r="2.5"/>
      <circle cx="520" cy="680" r="2"/><circle cx="50" cy="1050" r="2"/>
    </g>
  </svg>

  <p class="subtitle">「警察官に、なってみませんか」</p>
  <h1 class="title">女性警察官募集</h1>
</main>
</body>
</html>
```